KLD Photography Editing & Support Services for Real Estate

We require a double sided A4 flyer to promote our photography services to real estate agencies.
This particular service is targeted to rural areas where reliable, professional and highly skilled photographers are difficult to source. We teach the agent how to photograph, they upload files to a server and we take care of the rest (image editing, quality control and delivery). This will give the agents flexibility with when to shoot and eliminates the stress of managing a photographer / contractor. We offer a 1 day face to face training session and competitive packages for equipment start up.
We would like the flyer to look clean & very professional. The flyer should showcase samples of our work to highlight what can be achieved by using our services. We like the look of a black or dark background behind the text and feel that would look nice with our photographs provided. Otherwise open to your suggestions and ideas.
TEXT FOR FLYER:
Welcome to the KLD Real Estate Photography Editing and Support Service
• Take your real estate business to the next level by providing impressive real estate imagery that makes you stands out from the competition
• Omit the stress of trying to find a good photographer or managing an unreliable one and hence have more time to focus on other aspects of your business
• Showcase your listings with better quality and more impactful photographs than your competitors thereby increasing potential for a quick sale
• Great first impressions matter and you will achieve this by looking and feeling more professional. This will attract and retain more future clients.
HOW IT WORKS
• We understand that your time is valuable, so let us handle the editing and delivery of your images. You shoot, and we take care of the rest.
• Images are edited and delivered within 1 working day
INCLUSIONS:
• Full day face to face training (we come to you) and instructional handbook
• We will teach you everything you need to know about your equipment and how to take stunning real estate photographs
• Service turnaround within 1 working day
• Free HELP desk service Mon-Fri
• 12 month Exclusivity (rural towns only) for a limited time
INVESTMENT
• 99 per listing for us to manage images including editing, quality control and delivery (10 Images)
• Ask us about competitive packages for photography equipment if required
SUMMARY
The KLD Real Estate Photography Editing and Support Service is the perfect solution for busy real estate professionals who want to take their business to the next level. Our service is affordable, flexible, and designed to help you showcase your listings in the best possible light.
Contact us today to learn more about how we can help you.

```html
<!DOCTYPE html>
<html lang="en">
<head>
<meta charset="utf-8">
<title>KLD Real Estate Photography Flyer</title>
<link href="https://fonts.googleapis.com/css2?family=Montserrat:wght@600;700;800&family=Open+Sans:wght@400;600&display=swap" rel="stylesheet">
<style>
  :root{
    --stage:#5f5b73;
    --ink:#2a2341;
    --ink-deep:#1f1933;
    --blue:#2f9be0;
    --paper:#ffffff;
    --muted:#5a566a;
    --light:#e9e7f0;
    --photo-a:#b9b3a8;
    --photo-b:#6e6a66;
  }
  *{margin:0;padding:0;box-sizing:border-box}
  html,body{width:742px;height:1200px;overflow:hidden;background:var(--stage)}
  body{position:relative;font-family:"Open Sans",sans-serif}
  .page{position:absolute;top:352px;width:350px;height:495px;overflow:hidden}
  .page--front{left:10px;background:var(--paper);color:var(--muted)}
  .page--back{left:382px;background:var(--ink);color:var(--light)}
  .brand{position:absolute;top:30px;left:0;width:100%;display:flex;align-items:center;justify-content:center;gap:8px}
  .brand__dot{width:10px;height:10px;border-radius:50%}
  .brand__name{font-family:"Montserrat",sans-serif;font-weight:700;font-size:16px;line-height:1}
  .page--front .brand__name{color:var(--ink)}
  .page--front .brand__dot{background:var(--ink)}
  .page--back .brand__name{color:#fff}
  .page--back .brand__dot{background:#fff}
  .pill{position:absolute;background:var(--blue);color:#fff;font-family:"Montserrat",sans-serif;font-weight:700;font-size:6.5px;padding:3px 8px;border-radius:8px}
  .bullets{position:absolute;list-style:none;font-size:5.3px;line-height:1.45}
  .bullets li{position:relative;padding-left:7px;margin-bottom:4px}
  .bullets li::before{content:"";position:absolute;left:0;top:2.5px;width:3px;height:3px;border-radius:50%;background:var(--blue)}
  .photo{position:absolute}
  .welcome{position:absolute;left:184px;top:80px;width:150px;font-family:"Montserrat",sans-serif;font-weight:800;font-size:13px;line-height:1.15;color:var(--ink)}
  .welcome em{font-style:normal;color:var(--blue)}
  .summary-disc{position:absolute;left:190px;top:168px;width:140px;height:140px;border-radius:50%;background:var(--ink);color:#fff;display:flex;align-items:center;justify-content:center;text-align:center;padding:20px;font-size:5.6px;line-height:1.5}
  .contact{position:absolute;color:#fff;font-family:"Montserrat",sans-serif;font-weight:600;font-size:7px;line-height:1.35;text-align:center}
  .contact__phone{display:block;margin-top:4px;font-size:7.5px;font-weight:700}
  .section-title{position:absolute;left:20px;font-family:"Montserrat",sans-serif;font-weight:800;font-size:11px;color:#fff;letter-spacing:.5px}
  .section-title::after{content:"";display:block;width:120px;height:2px;margin-top:3px;background:var(--blue)}
  .frame{position:absolute;border:3px solid #fff;background:linear-gradient(135deg,var(--photo-a),var(--photo-b))}
</style>
</head>
<body>

<section class="page page--front">
  <div class="brand">
    <span class="brand__dot"></span>
    <span class="brand__name">Kara Dunmore</span>
  </div>

  <span class="pill" style="left:18px;top:84px">KLD Real Estate</span>
  <ul class="bullets" style="left:18px;top:104px;width:155px">
    <li>Take your real estate business to the next level by providing impressive real estate imagery that makes you stand out from the competition</li>
    <li>Omit the stress of trying to find a good photographer or managing an unreliable one and hence have more time to focus on other aspects of your business</li>
    <li>Showcase your listings with better quality and more impactful photographs than your competitors thereby increasing potential for a quick sale</li>
    <li>Great first impressions matter and you will achieve this by looking and feeling more professional. This will attract and retain more future clients.</li>
  </ul>

  <div class="photo" role="img" aria-label="Sample real estate photograph of a modern home" style="left:18px;top:236px;width:155px;height:90px;background:linear-gradient(160deg,#d6dbe0,#8a8378 60%,#4a4540)"></div>

  <h1 class="welcome">Welcome to the <em>KLD Real Estate Photography Editing</em> and <em>Support Service</em></h1>

  <span class="pill" style="left:232px;top:150px;font-size:8px;padding:3px 12px">SUMMARY</span>
  <p class="summary-disc">The KLD Real Estate Photography Editing and Support Service is the perfect solution for busy real estate professionals who want to take their business to the next level. Our service is affordable, flexible, and designed to help you showcase your listings in the best possible light.</p>

  <div class="photo" role="img" aria-label="Exterior photograph of a contemporary house at dusk" style="left:0;top:330px;width:350px;height:165px;background:linear-gradient(170deg,#c9ccd2,#7d7872 55%,#3f3a3a)"></div>
  <svg class="photo" style="left:0;top:330px" width="350" height="165" viewBox="0 0 350 165" aria-hidden="true">
    <path d="M0 120 C80 95 140 150 210 125 C260 108 310 90 350 100 L350 165 L0 165 Z" fill="var(--ink)" opacity=".92"/>
    <path d="M200 0 C230 30 250 60 350 40 L350 165 L230 165 C250 110 210 60 200 0 Z" fill="var(--ink-deep)" opacity=".85"/>
  </svg>
  <p class="contact" style="left:236px;top:360px;width:104px">Contact us today to learn more about how we can help you.<span class="contact__phone">000 0000 0000</span></p>
</section>

<section class="page page--back">
  <div class="brand">
    <span class="brand__dot"></span>
    <span class="brand__name">Kara Dunmore</span>
  </div>

  <h2 class="section-title" style="top:86px">HOW IT WORKS</h2>
  <ul class="bullets" style="left:20px;top:108px;width:180px">
    <li>We understand that your time is valuable, so let us handle the editing and delivery of your images. You shoot, and we take care of the rest.</li>
    <li>Images are edited and delivered within 1 working day</li>
  </ul>

  <h2 class="section-title" style="top:168px">INCLUSIONS:</h2>
  <ul class="bullets" style="left:20px;top:190px;width:180px">
    <li>Full day face to face training (we come to you) and instructional handbook</li>
    <li>We will teach you everything you need to know about your equipment and how to take stunning real estate photographs</li>
    <li>Service turnaround within 1 working day</li>
    <li>Free HELP desk service Mon-Fri</li>
    <li>12 month Exclusivity (rural towns only) for a limited time</li>
  </ul>

  <h2 class="section-title" style="top:300px">INVESTMENT</h2>
  <ul class="bullets" style="left:20px;top:322px;width:180px">
    <li>99 per listing for us to manage images including editing, quality control and delivery (10 Images)</li>
    <li>Ask us about competitive packages for photography equipment if required</li>
  </ul>

  <div class="frame" role="img" aria-label="Sample interior photograph of a living room" style="left:214px;top:96px;width:60px;height:48px"></div>
  <div class="frame" role="img" aria-label="Sample interior photograph of a kitchen" style="left:278px;top:96px;width:56px;height:48px"></div>
  <div class="frame" role="img" aria-label="Sample exterior photograph of a home" style="left:214px;top:150px;width:120px;height:62px"></div>
  <div class="frame" role="img" aria-label="Sample interior photograph of a dining area" style="left:214px;top:218px;width:60px;height:50px"></div>
  <div class="frame" role="img" aria-label="Sample interior photograph of a bedroom" style="left:278px;top:218px;width:56px;height:50px"></div>

  <p class="contact" style="left:214px;top:318px;width:120px">Contact us today to learn more about how we can help you.<span class="contact__phone">000 0000 0000</span></p>
</section>

</body>
</html>
```